Your Road Counsel Billboard Design for Personal Injury Law Firm

Need a billboard design that we can use for different versions. 1400px X 400px jpeg or png
I have attached the logo and the attorney for the billboard. Attorney Dana Whitfield
Here is a link to our current website yourroadcounsel-example.com

HEADLINE: HIT BY A TRUCK?
SUBHEAD: NO FEE. BIG FIGHT.
855-MARGOT-7

HEADLINE: ACCIDENT?
SUBHEAD: NO FEE, UNLESS WE WIN!
855-MARGOT-7

HEADLINE: BIG TRUCK. BIG CASE.
SUBHEAD: YOU PAY $0 UPFRONT
855-MARGOT-7

Target Market(s)

People in Car Accident

Industry/Entity Type

Personal Injury Attorneys

```html
<!DOCTYPE html>
<html lang="en">
<head>
<meta charset="utf-8">
<title>Your Road Counsel — Hit by a Truck Billboard</title>
<link rel="stylesheet" href="https://fonts.googleapis.com/css2?family=Poppins:wght@500;700;800&display=swap">
<style>
  :root {
    --page-bg: #e6e6e6;
    --board-bg: #050505;
    --ink-white: #ffffff;
    --ink-black: #0b0b0b;
    --brand-green: #5fd34a;
    --photo-dark: #1a1a1a;
    --photo-mid: #6b6b6b;
    --photo-light: #b9bcc4;
    --car-steel: #7b8496;
  }
  * { box-sizing: border-box; margin: 0; padding: 0; }
  html, body {
    width: 1200px;
    height: 525px;
    overflow: hidden;
    background: var(--page-bg);
    font-family: "Poppins", Arial, sans-serif;
  }
  .billboard {
    position: absolute;
    left: 20px;
    top: 97px;
    width: 1160px;
    height: 331px;
    background: var(--board-bg);
    overflow: hidden;
  }
  .street-photo {
    position: absolute;
    left: 540px;
    top: 0;
    width: 620px;
    height: 331px;
    background:
      radial-gradient(ellipse 210px 110px at 360px 210px, var(--car-steel) 0%, rgba(90,96,110,0.6) 55%, rgba(0,0,0,0) 100%),
      linear-gradient(180deg, #9a9a9a 0%, var(--photo-mid) 25%, var(--photo-dark) 70%, #0d0d0d 100%);
    -webkit-mask-image: linear-gradient(90deg, transparent 0%, #000 35%);
    mask-image: linear-gradient(90deg, transparent 0%, #000 35%);
  }
  .headline {
    position: absolute;
    left: 60px;
    top: 36px;
    width: 560px;
    text-align: center;
    text-transform: uppercase;
    font-weight: 800;
    line-height: 1;
  }
  .headline__lead {
    display: block;
    color: var(--ink-white);
    font-size: 56px;
    letter-spacing: -0.5px;
  }
  .headline__key {
    display: block;
    color: var(--brand-green);
    font-size: 110px;
    letter-spacing: -2px;
    margin-top: -4px;
  }
  .subhead {
    position: absolute;
    left: 60px;
    top: 182px;
    width: 560px;
    text-align: center;
    font-weight: 800;
    font-size: 35px;
    line-height: 1;
    color: var(--ink-white);
    text-transform: uppercase;
  }
  .subhead__accent { color: var(--brand-green); }
  .firm-name {
    position: absolute;
    left: 38px;
    top: 250px;
    display: flex;
    align-items: center;
    gap: 10px;
    color: var(--ink-white);
    font-weight: 700;
    font-size: 19px;
    line-height: 1;
    text-transform: uppercase;
  }
  .firm-name__dot {
    width: 16px;
    height: 16px;
    border-radius: 50%;
    background: var(--brand-green);
  }
  .phone-pill {
    position: absolute;
    left: 287px;
    top: 240px;
    width: 500px;
    height: 55px;
    border-radius: 28px 0 0 28px;
    background: linear-gradient(90deg, #ffffff 0%, #ffffff 55%, rgba(255,255,255,0.6) 80%, rgba(255,255,255,0) 100%);
    display: flex;
    align-items: center;
    padding-left: 10px;
    gap: 12px;
  }
  .phone-pill__icon { width: 30px; height: 30px; flex: none; }
  .phone-pill__number {
    color: var(--ink-black);
    font-weight: 800;
    font-size: 39px;
    letter-spacing: -0.5px;
    line-height: 1;
  }
</style>
</head>
<body>
  <main class="billboard">
    <div class="street-photo" role="img" aria-label="Wrecked silver car with a crushed front end on a motion-blurred city street"></div>

    <h1 class="headline">
      <span class="headline__lead">Hit by a</span>
      <span class="headline__key">Truck?</span>
    </h1>
    <p class="subhead">No <span class="subhead__accent">Fee.</span> Big <span class="subhead__accent">Fight</span></p>

    <div class="firm-name">
      <span class="firm-name__dot"></span>
      <span>Your Road Counsel</span>
    </div>

    <div class="phone-pill">
      <svg class="phone-pill__icon" viewBox="0 0 30 30" aria-hidden="true">
        <circle cx="15" cy="15" r="15" fill="var(--brand-green)"/>
        <path d="M10.5 8.5c.6-.6 1.5-.5 1.9.2l1.3 2.2c.3.6.2 1.3-.3 1.7l-.9.8c.8 1.8 2.2 3.2 4 4l.8-.9c.4-.5 1.1-.6 1.7-.3l2.2 1.3c.7.4.8 1.3.2 1.9l-1 1c-.9.9-2.3 1.1-3.5.5-3.4-1.6-6.1-4.3-7.7-7.7-.6-1.2-.4-2.6.5-3.5z" fill="var(--ink-black)"/>
      </svg>
      <span class="phone-pill__number">855-MARGOT-7</span>
    </div>
  </main>
</body>
</html>
```